Bright Path Rehabilitation Stationary
Business Card, Letter Head, Envelope, Fax Cover, Invoice & Referral/Prescription Pad
Bright Path Rehabilitation Stationary  -
Creative Brief
Use specific fonts
Please use standard or same font as in logo
Simple
Gregory Lindqvist
Marketing/Administrative Director
27415 PT Hargrove Blvd # D Palo Mesa North, AZ 85291
gregory@brightpathrehab.com
www.brightpathrehab.com
Please include on the front of the card "Comprehensive Outpatient Rehabilitation Facility".Physical Therapy and Psych/Social Services. Please draw up another business card with same information except Monica Lindqvist with a title of Physical Therapist. For the fax cover sheet, envelope, referral/prescription pad and letter head please incorporate logo. We have included a map as well for referral/prescription pads.
Hands on Approach Individualized Plan of Care Friendly, Caring Staff

```html
<!DOCTYPE html>
<html lang="en">
<head>
<meta charset="utf-8">
<title>Bright Path Rehabilitation Stationery</title>
<link rel="stylesheet" href="https://fonts.googleapis.com/css2?family=Open+Sans:wght@400;600;700&display=swap">
<style>
  :root {
    --bg: #ecebe8;
    --paper: #ffffff;
    --blue: #2e5fb8;
    --blue-deep: #1c2f8f;
    --grey: #8f949c;
    --grey-light: #d9dce1;
    --ink: #3a3d44;
    --ink-soft: #7b8089;
    --black: #141518;
    --card-grey: #6e7177;
  }
  * { margin: 0; padding: 0; box-sizing: border-box; }
  html, body { width: 1200px; height: 713px; overflow: hidden; }
  body { background: var(--bg); font-family: "Open Sans", Arial, sans-serif; color: var(--ink); position: relative; }

  .sheet { position: absolute; background: var(--paper); box-shadow: 0 2px 8px rgba(0,0,0,.18); overflow: hidden; }
  .letterhead { width: 250px; height: 324px; top: 40px; }
  .letterhead--one { left: 40px; }
  .letterhead--two { left: 580px; }
  .fax-cover { width: 250px; height: 324px; top: 40px; left: 310px; }

  .corner-curve { position: absolute; left: 0; top: 0; width: 90px; height: 90px; }
  .brand { position: absolute; display: flex; align-items: center; gap: 5px; font-weight: 600; color: var(--blue); letter-spacing: .04em; text-transform: uppercase; }
  .brand-dot { width: 9px; height: 9px; border-radius: 50%; background: var(--blue); flex: none; }
  .sheet .brand { top: 26px; left: 56px; font-size: 8px; }
  .sheet-rule { position: absolute; top: 52px; left: 56px; right: 14px; height: 1px; background: var(--blue); opacity: .6; }
  .sheet-footer { position: absolute; bottom: 12px; left: 14px; right: 14px; border-top: 1px solid var(--grey-light); padding-top: 4px; font-size: 5px; color: var(--ink-soft); text-align: center; line-height: 1.5; }

  .fax-title { position: absolute; top: 20px; right: 16px; font-size: 16px; font-weight: 700; color: var(--ink); letter-spacing: .08em; }
  .fax-fields { position: absolute; top: 72px; left: 20px; right: 20px; border-collapse: collapse; font-size: 6px; }
  .fax-fields th { text-align: left; width: 32px; padding: 5px 4px; background: var(--grey-light); font-weight: 600; color: var(--ink); }
  .fax-fields td { border-bottom: 1px solid var(--grey-light); }
  .fax-checks { position: absolute; top: 230px; left: 20px; right: 20px; display: grid; grid-template-columns: 1fr 1fr; gap: 6px; font-size: 6px; color: var(--ink); }
  .fax-checks span::before { content: ""; display: inline-block; width: 6px; height: 6px; border: 1px solid var(--grey); margin-right: 4px; vertical-align: -1px; }

  .envelope { width: 320px; height: 150px; top: 40px; left: 850px; }
  .envelope .brand { top: 20px; left: 58px; font-size: 8px; }
  .envelope-return { position: absolute; top: 36px; left: 58px; font-size: 5.5px; color: var(--ink-soft); line-height: 1.5; }
  .envelope-rule { position: absolute; bottom: 16px; left: 14px; right: 14px; height: 1px; background: var(--blue); opacity: .6; }

  .card { position: absolute; width: 156px; height: 90px; border-radius: 4px; box-shadow: 0 2px 6px rgba(0,0,0,.25); overflow: hidden; }
  .card .brand { font-size: 6.5px; }
  .card-line { font-size: 5px; line-height: 1.55; }
  .card--grey { left: 850px; top: 214px; background: var(--card-grey); color: #fff; }
  .card--grey .brand { color: #fff; top: 30px; left: 16px; }
  .card--grey .brand-dot { background: #fff; }
  .card--grey .tagline { position: absolute; top: 48px; left: 16px; right: 12px; font-size: 5px; color: #e6e8ec; line-height: 1.5; }
  .card--blue { left: 1014px; top: 214px; background: var(--blue-deep); color: #fff; padding: 12px 12px; }
  .card--blue .brand { color: #fff; position: static; margin-bottom: 10px; }
  .card--blue .brand-dot { background: #fff; }
  .card--black { left: 850px; top: 320px; background: var(--black); color: #fff; padding: 12px 12px 12px 46px; }
  .card--black .corner-curve { width: 40px; height: 90px; }
  .card--black .card-name { font-size: 7px; font-weight: 700; color: #fff; }
  .card--black .card-title { font-size: 5.5px; color: #8fb0ee; margin-bottom: 8px; }
  .card--black-back { left: 1014px; top: 320px; background: var(--black); display: flex; flex-direction: column; align-items: center; justify-content: center; gap: 6px; }
  .card--black-back .brand { position: static; color: #8fb0ee; }
  .card--black-back .brand-dot { background: #8fb0ee; }
  .card--black-back .card-line { color: #b9bcc3; text-align: center; }
  .card-name { font-size: 7px; font-weight: 700; }
  .card-title { font-size: 5.5px; color: #c9d6f3; margin-bottom: 6px; }
</style>
</head>
<body>

<svg width="0" height="0" aria-hidden="true" style="position:absolute">
  <defs>
    <symbol id="corner" viewBox="0 0 90 90">
      <path d="M0 0 H48 C22 18 14 50 24 90 H0 Z" fill="#2e5fb8"/>
      <path d="M48 0 H58 C32 20 26 54 36 90 H24 C14 50 22 18 48 0 Z" fill="#a7abb2"/>
    </symbol>
  </defs>
</svg>

<section class="sheet letterhead letterhead--one">
  <svg class="corner-curve" aria-hidden="true"><use href="#corner"/></svg>
  <div class="brand"><span class="brand-dot"></span>Bright Path Rehabilitation</div>
  <div class="sheet-rule"></div>
  <div class="sheet-footer">27415 PT Hargrove Blvd # D, Palo Mesa North, AZ 85291<br>www.brightpathrehab.com</div>
</section>

<section class="sheet fax-cover">
  <svg class="corner-curve" aria-hidden="true"><use href="#corner"/></svg>
  <div class="brand"><span class="brand-dot"></span>Bright Path Rehabilitation</div>
  <div class="fax-title">FAX</div>
  <table class="fax-fields">
    <tr><th>To</th><td></td></tr>
    <tr><th>From</th><td></td></tr>
    <tr><th>Fax</th><td></td></tr>
    <tr><th>Phone</th><td></td></tr>
    <tr><th>Date</th><td></td></tr>
    <tr><th>Pages</th><td></td></tr>
    <tr><th>Re</th><td></td></tr>
  </table>
  <div class="fax-checks">
    <span>Urgent</span><span>For Review</span>
    <span>Please Comment</span><span>Please Reply</span>
  </div>
  <div class="sheet-footer">27415 PT Hargrove Blvd # D, Palo Mesa North, AZ 85291<br>www.brightpathrehab.com</div>
</section>

<section class="sheet letterhead letterhead--two">
  <svg class="corner-curve" aria-hidden="true"><use href="#corner"/></svg>
  <div class="brand"><span class="brand-dot"></span>Bright Path Rehabilitation</div>
  <div class="sheet-rule"></div>
  <div class="sheet-footer">27415 PT Hargrove Blvd # D, Palo Mesa North, AZ 85291<br>www.brightpathrehab.com</div>
</section>

<section class="sheet envelope">
  <svg class="corner-curve" aria-hidden="true"><use href="#corner"/></svg>
  <div class="brand"><span class="brand-dot"></span>Bright Path Rehabilitation</div>
  <div class="envelope-return">27415 PT Hargrove Blvd # D<br>Palo Mesa North, AZ 85291</div>
  <div class="envelope-rule"></div>
</section>

<article class="card card--grey">
  <div class="brand"><span class="brand-dot"></span>Bright Path Rehabilitation</div>
  <p class="tagline">Comprehensive Outpatient Rehabilitation Facility<br>Physical Therapy and Psych/Social Services</p>
</article>

<article class="card card--blue">
  <div class="brand"><span class="brand-dot"></span>Bright Path Rehabilitation</div>
  <p class="card-name">Monica Lindqvist</p>
  <p class="card-title">Physical Therapist</p>
  <p class="card-line">27415 PT Hargrove Blvd # D<br>Palo Mesa North, AZ 85291<br>www.brightpathrehab.com</p>
</article>

<article class="card card--black">
  <svg class="corner-curve" viewBox="0 0 40 90" preserveAspectRatio="none" aria-hidden="true">
    <path d="M0 0 H26 C12 24 10 60 18 90 H0 Z" fill="#2e5fb8"/>
    <path d="M26 0 H32 C18 26 16 60 24 90 H18 C10 60 12 24 26 0 Z" fill="#a7abb2"/>
  </svg>
  <p class="card-name">Gregory Lindqvist</p>
  <p class="card-title">Marketing/Administrative Director</p>
  <p class="card-line">27415 PT Hargrove Blvd # D<br>Palo Mesa North, AZ 85291<br>gregory@brightpathrehab.com<br>www.brightpathrehab.com</p>
</article>

<article class="card card--black-back">
  <div class="brand"><span class="brand-dot"></span>Bright Path Rehabilitation</div>
  <p class="card-line">Hands on Approach · Individualized Plan of Care<br>Friendly, Caring Staff</p>
</article>

</body>
</html>
```